Charting the steady harbor route is a show dedicated to helping plan fiduciaries close the gap between ERISA participant disclosures and employees, understanding, and attaining actual knowledge of their plan.

Target Market(s)

Retirement Plan Sponsors

Industry/Entity Type

Financial

Colors
0054AA
0677BA
7BADD7
CADEEF
E8F1F8

Requirements
Must have
• Charting the Steady Harbor Route

```html
<!DOCTYPE html>
<html lang="en">
<head>
<meta charset="utf-8">
<title>Charting the Steady Harbor Route</title>
<link rel="stylesheet" href="https://fonts.googleapis.com/css2?family=Montserrat:wght@300;600;700;800&display=swap">
<style>
  :root {
    --brand-blue: #0054AA;
    --white: #FFFFFF;
    --portrait-dark: #1c2433;
    --portrait-mid: #6f7c90;
    --portrait-light: #c9ced6;
  }
  html, body {
    margin: 0;
    padding: 0;
    width: 1200px;
    height: 1200px;
    overflow: hidden;
    background: var(--brand-blue);
  }
  .cover {
    position: relative;
    width: 1200px;
    height: 1200px;
    background: var(--brand-blue);
    overflow: hidden;
    font-family: "Montserrat", sans-serif;
    color: var(--white);
  }
  .frame-line {
    position: absolute;
    background: var(--white);
  }
  .frame-top { left: 26px; top: 25px; width: 1149px; height: 2px; }
  .frame-right { left: 1173px; top: 25px; width: 2px; height: 1150px; }
  .frame-left { left: 25px; top: 25px; width: 2px; height: 796px; }
  .frame-bottom { left: 773px; top: 1173px; width: 402px; height: 2px; }

  .host-portrait {
    position: absolute;
    left: 0;
    top: 224px;
    width: 751px;
    height: 976px;
    display: block;
  }

  .title {
    position: absolute;
    left: 518px;
    top: 0;
    margin: 0;
    font-weight: 400;
  }
  .title-line {
    position: absolute;
    left: 0;
    white-space: nowrap;
    font-size: 86px;
    line-height: 1;
    text-transform: uppercase;
    letter-spacing: -1px;
  }
  .title-line.bold { font-weight: 700; }
  .title-line.light { font-weight: 300; }
  .line-1 { top: 270px; }
  .line-2 { top: 353px; }
  .line-3 { top: 438px; }
  .line-4 { top: 522px; }

  .title-rule {
    position: absolute;
    left: 860px;
    top: 566px;
    width: 268px;
    height: 2px;
    background: var(--white);
  }

  .mic-icon {
    position: absolute;
    left: 1064px;
    top: 276px;
    width: 90px;
    height: 180px;
  }

  .host-badge {
    position: absolute;
    left: 525px;
    top: 624px;
    width: 612px;
    height: 56px;
    background: var(--white);
    color: var(--brand-blue);
    display: flex;
    align-items: center;
    justify-content: center;
    font-weight: 600;
    font-size: 33px;
  }
</style>
</head>
<body>
  <main class="cover">
    <div class="frame-line frame-top"></div>
    <div class="frame-line frame-right"></div>
    <div class="frame-line frame-left"></div>
    <div class="frame-line frame-bottom"></div>

    <svg class="host-portrait" viewBox="0 0 751 976" role="img" aria-label="Portrait of the show host in a dark suit, white shirt and patterned gold and blue tie">
      <defs>
        <linearGradient id="portraitTone" x1="0" y1="0" x2="0" y2="1">
          <stop offset="0" stop-color="#c9ced6"/>
          <stop offset="0.45" stop-color="#9a8f86"/>
          <stop offset="0.62" stop-color="#2a3142"/>
          <stop offset="1" stop-color="#1c2433"/>
        </linearGradient>
      </defs>
      <path d="M56,230 C56,60 160,0 270,0 C400,0 481,80 481,230 L481,466 L680,466 Q751,466 751,540 L751,976 L0,976 L0,660 Q40,540 110,510 Q66,400 56,230 Z" fill="url(#portraitTone)"/>
    </svg>

    <h1 class="title">
      <span class="title-line bold line-1">Charting</span>
      <span class="title-line light line-2">The Steady</span>
      <span class="title-line bold line-3">Harbor</span>
      <span class="title-line bold line-4">Route</span>
    </h1>

    <div class="title-rule"></div>

    <svg class="mic-icon" viewBox="0 0 90 180" aria-hidden="true">
      <rect x="18" y="4" width="54" height="92" rx="27" fill="#FFFFFF"/>
      <g stroke="#0054AA" stroke-width="5" stroke-linecap="round">
        <line x1="28" y1="32" x2="46" y2="32"/>
        <line x1="28" y1="46" x2="46" y2="46"/>
        <line x1="28" y1="60" x2="46" y2="60"/>
        <line x1="28" y1="74" x2="46" y2="74"/>
      </g>
      <path d="M6 56 V70 A39 39 0 0 0 84 70 V56" fill="none" stroke="#FFFFFF" stroke-width="7" stroke-linecap="round"/>
      <line x1="45" y1="110" x2="45" y2="176" stroke="#FFFFFF" stroke-width="7"/>
    </svg>

    <div class="host-badge">Hosted by&nbsp; Glen</div>
  </main>
</body>
</html>
```